Velmoria sailing boat for love and romance seekers*

We will pay extra 200$ for the winning design! So, we have a sailing boat, Halvard 58 KT called Velmoria, which we’d like to give for charter in Turkey and maybe other countries. Need a dedicated web page, with gallery, calendar, videos, customer reviews, possibility to pay down payment, legal disclosures and in 3 languages (English, Russian and Turkish). Also, there should be info on toys and crew. We can also agree on a monthly fee for maintenance and updates. It’s really important to show the details, so that potential customers can see clearly that the boat is in perfect shape. If needed, we can even make a 3D of the interior, or any other materials that you might need. People should also have the possibility to see the sailing routes that they can chose and experience while cruising. Additionally, we can organize diving tours, surfing lessons, and any other activities.

Target Market(s)

Family with kids. Those people that are looking for more luxury than what’s usually offered with other boats. This is a middle segment between usual boats and super luxury boats. Also, it’s for those people that want romance, love and are looking for Unforgetable experiences with their family.

Coding

Coded - Design and coding required

Number of Pages Required

3 page

Font styles to use
Sans Serif

Requirements
Must have
• Boat has lots of options, and we have a tender boat with which one can waterski, pull ringos and other toys. It’s big enough to carry all guests at the same time and comfortable to reach safely any remote beach location. We have brand new snorkeling and diving equipment, new paddle and surfing boards, new zumflo, Fintrak and life jackets for all age groups. Also, we should have a page on crew, who they are and whom additionally they can chose (for example cook or cleaning staff).
Nice to have
• We’d like to see a page with will make you dream, feel romantic and in love. To ensure the visitors that our boat is perfect for a dream holiday. Imagine being in a secluded white sand beach bay all alone with your loved ones, in a beautiful luxurious boat. Now stop dreaming and join us to make your dreams come true. Lastly, because of virus, we should also mention that we do proper cleaning of boat after every use (COVID free).

Velmōria is a Sanskrit word that means "wandering" or "world", with the connotation of cyclic, circuitous change. It is also the concept of rebirth and "cyclicality of all life, matter, existence", a fundamental belief of most Indian religions. In short, it is the cycle of death and rebirth.
Should not have
• It should not be only for one system, all devices should be able to see that page properly.

```html
<!DOCTYPE html>
<html lang="en">
<head>
<meta charset="utf-8">
<title>Velmoria — Snorkeling</title>
<link href="https://fonts.googleapis.com/css2?family=Nunito+Sans:ital,wght@0,400;0,600;0,700;0,800;1,400&display=swap" rel="stylesheet">
<style>
:root{
  --ink:#2d4a45;
  --deep:#0d5a45;
  --teal:#00e5b4;
  --aqua-line:#8fe9ef;
  --mist:#e9fbfd;
  --muted:#6b7c79;
  --orange:#ffa619;
  --white:#ffffff;
}
*{box-sizing:border-box;margin:0;padding:0}
html,body{width:1200px;height:4434px;overflow:hidden;background:var(--white)}
body{position:relative;font-family:"Nunito Sans",sans-serif;color:var(--ink)}
.abs{position:absolute}
.photo{position:absolute}
.site-header{left:98px;top:31px;width:1002px;height:69px;background:var(--white);box-shadow:0 8px 22px rgba(0,0,0,.12)}
.logo{position:absolute;left:26px;top:16px;font-size:30px;font-weight:600;color:var(--deep);letter-spacing:.5px}
.nav a{position:absolute;top:24px;font-size:15px;font-weight:600;color:#3a4a48;text-decoration:none}
.lang{position:absolute;left:961px;top:29px;width:18px;height:12px;background:#d94a4a;border-radius:2px}
.hero-main{left:420px;top:164px;width:355px;height:409px;background:linear-gradient(160deg,#3fc6c4,#1a9aa2 60%,#2bb7b3);box-shadow:0 24px 40px rgba(0,0,0,.28)}
.bookmark{left:451px;top:158px;width:52px;height:61px;background:var(--teal);clip-path:polygon(0 0,100% 0,100% 100%,50% 82%,0 100%)}
.hero-2{left:787px;top:193px;width:306px;height:355px;background:linear-gradient(180deg,#2d6fd1,#1a3f9e)}
.hero-3{left:1112px;top:193px;width:88px;height:355px;background:linear-gradient(180deg,#2d5e8f,#5c8fb0)}
.tabs span{position:absolute;top:665px;font-size:19px;color:#4e5f5c;white-space:nowrap}
.tab-active{left:522px;top:656px;width:155px;height:48px;border:2px solid var(--aqua-line);border-radius:24px;background:var(--white)}
.tab-active::before{content:"";position:absolute;left:67px;top:-9px;width:12px;height:12px;background:var(--white);border-left:2px solid var(--aqua-line);border-top:2px solid var(--aqua-line);transform:rotate(45deg)}
.page-title{left:0;width:1196px;top:770px;text-align:center;font-size:65px;font-weight:800;color:var(--ink)}
.intro-card{left:110px;top:944px;width:444px;height:465px;background:var(--white);box-shadow:0 6px 30px rgba(0,0,0,.08)}
.mask-art{left:160px;top:895px;width:133px;height:135px;background:#d9dcdc;border-radius:6px}
.intro-text{left:160px;top:1064px;width:345px;font-size:16px;line-height:31.7px;color:#4d5d5a}
.intro-quote{left:160px;top:1290px;font-size:19px;line-height:33px;font-style:italic;color:#3a4a48}
.video{left:599px;top:1007px;width:488px;height:285px;background:linear-gradient(180deg,#8d9fb0,#a8b4c0 40%,#4f6a82 55%,#7a6a60);box-shadow:0 18px 36px rgba(0,0,0,.2)}
.play{left:832px;top:1124px;width:0;height:0;border-left:22px solid var(--white);border-top:13px solid transparent;border-bottom:13px solid transparent}
.progress{left:637px;top:1265px;width:413px;height:3px;background:rgba(255,255,255,.45)}
.progress i{display:block;width:124px;height:3px;background:var(--white)}
.crew-photo{left:0;top:1631px;width:558px;height:373px;background:linear-gradient(120deg,#4aa6c0,#6b7a6e 45%,#2a3440)}
.section-h{font-size:31px;font-weight:600;color:var(--ink)}
.crew-text{left:611px;top:1786px;width:486px;font-size:15.5px;line-height:31.7px;color:#5a6a67}
.eq-title{left:0;width:1198px;top:2185px;text-align:center;font-size:34px;font-weight:600;color:var(--ink)}
.band{left:0;top:2273px;width:1200px;height:835px;background:var(--mist);clip-path:polygon(0 121px,100% 0,100% 724px,0 835px)}
.book-title{left:117px;top:3193px;font-size:62px;font-weight:800;color:var(--deep)}
.form-card{left:112px;top:3341px;width:475px;height:513px;background:var(--white);box-shadow:0 10px 40px rgba(0,0,0,.09)}
.field{position:absolute;border-bottom:2px solid #a7ece9;height:34px;font-size:12px;color:#9aa7a5;padding:6px 0 0 30px}
.field svg{position:absolute;left:6px;top:6px}
.cta{left:179px;top:3764px;width:329px;height:49px;background:var(--orange);color:var(--white);font-size:16px;font-weight:700;text-align:center;line-height:49px;border-radius:2px}
.pay{position:absolute;top:3717px;font-size:12px;font-weight:800;color:#333}
.cal-head{left:656px;top:3341px;width:417px;height:38px;background:var(--teal);color:var(--deep);font-size:19px;text-align:center;line-height:38px}
.dow{position:absolute;top:3410px;font-size:12px;font-style:italic;color:#8a9896;width:30px;text-align:center}
.day{position:absolute;width:40px;text-align:center;font-size:21px;color:var(--ink)}
.range{left:706px;top:3513px;width:245px;height:55px;background:var(--teal);border-radius:28px;box-shadow:0 0 0 8px #fff,0 0 0 10px #9be8e0}
.footer{left:0;top:4041px;width:1200px;height:393px;background:linear-gradient(180deg,#06c69a 0,#0b8160 35%,#0b5a40 100%);color:var(--white)}
.footer .flogo{position:absolute;left:115px;top:75px;font-size:32px;font-weight:600}
.footer .addr{position:absolute;left:115px;top:144px;font-size:16px;line-height:27px}
.footer .social{position:absolute;top:234px;width:20px;height:20px;border-radius:50%;background:var(--white)}
.footer .copy{position:absolute;left:115px;top:270px;font-size:12px}
.footer ul{position:absolute;top:102px;list-style:none;font-size:16px;line-height:35px}
</style>
</head>
<body>

<div class="abs band"></div>

<header class="abs site-header">
  <div class="logo">Velmoria</div>
  <nav class="nav">
    <a style="left:442px">Facilities</a>
    <a style="left:568px">Toys</a>
    <a style="left:664px">Events</a>
    <a style="left:758px">Crew</a>
    <a style="left:853px">Inquiry</a>
  </nav>
  <span class="lang" role="img" aria-label="Language: English"></span>
</header>

<div class="photo hero-main" role="img" aria-label="Snorkeler floating in turquoise water"></div>
<div class="abs bookmark"></div>
<div class="photo hero-2" role="img" aria-label="Diver in deep blue water"></div>
<div class="photo hero-3" role="img" aria-label="Waterski on open sea"></div>

<div class="abs tab-active"></div>
<div class="tabs">
  <span style="left:557px">Snorkeling</span>
  <span style="left:715px">Diving</span>
  <span style="left:810px">Pull Ringos</span>
  <span style="left:968px">Waterski</span>
  <span style="left:1095px">Paddle &amp; Surf</span>
</div>

<h1 class="abs page-title">Snorkeling</h1>

<div class="abs intro-card"></div>
<div class="photo mask-art" role="img" aria-label="Sketch of a snorkel mask"></div>
<p class="abs intro-text">Snorkeling Pellentesque at tincidunt lorem, sollicitudin eleifend ante. Nunc vestibulum facilisis leo. Mauris iaculis suscipit ligula, nec luctus ligula pulvinar in.extended periods with relatively little effort and to breathe while face-down at the surface.</p>
<p class="abs intro-quote">Anytime you want,<br>Just snorkel!</p>

<div class="photo video" role="img" aria-label="Video: couple relaxing on the boat deck at sea"></div>
<div class="abs play"></div>
<div class="abs progress"><i></i></div>

<div class="photo crew-photo" role="img" aria-label="Crew instructing guests beside diving tanks"></div>
<h2 class="abs section-h" style="left:611px;top:1722px">Supporting Crew</h2>
<p class="abs crew-text">Sed eget condimentum quam. Nulla laoreet vestibulum condi-<br>mentum. Proin at ex id orci elementum imperdiet. Fusce fermen-<br>tum ac eros quis vestibulum. Curabitur sapien sem, tincidunt id<br>imperdiet sit amet, sodales vel metus.</p>

<h2 class="abs eq-title">Completly Snorkleing Equipment</h2>
<div class="photo" style="left:112px;top:2285px;width:306px;height:265px;background:linear-gradient(135deg,#3bb6d6 0,#d8b88e 30%,#c9a982)" role="img" aria-label="Swim goggles on sand"></div>
<div class="photo" style="left:112px;top:2578px;width:306px;height:265px;background:linear-gradient(90deg,#2fb9e6 0,#2fb9e6 30%,#f1e43a 40%)" role="img" aria-label="Snorkel set and bottle on yellow and blue"></div>
<div class="photo" style="left:112px;top:2874px;width:306px;height:150px;background:linear-gradient(135deg,#e8562a,#2a5a7a 60%,#e85aa0)" role="img" aria-label="Children in life jackets"></div>
<div class="photo" style="left:446px;top:2285px;width:306px;height:470px;background:linear-gradient(180deg,#b9bfc2,#6a7072 60%,#9aa1a4)" role="img" aria-label="Diving tanks with regulators"></div>
<div class="photo" style="left:446px;top:2781px;width:306px;height:241px;background:linear-gradient(135deg,#4aa6c0,#8a8f8f 50%,#2a2f33)" role="img" aria-label="Diving tank and gear by the pool"></div>
<div class="photo" style="left:780px;top:2285px;width:307px;height:355px;background:linear-gradient(135deg,#eeeae4,#f2c63a 50%,#e7e2da)" role="img" aria-label="Yellow swim fins"></div>
<div class="photo" style="left:780px;top:2667px;width:307px;height:357px;background:linear-gradient(180deg,#86cde6 0,#1aa3c4 25%,#e2d3bd 35%,#d4c2a6)" role="img" aria-label="Flip-flops and snorkel mask on the beach"></div>

<h2 class="abs book-title">Lets Pick Your Date</h2>
<div class="abs form-card"></div>
<div class="field" style="left:177px;top:3377px;width:334px">
  <svg width="14" height="16" viewBox="0 0 14 16"><circle cx="7" cy="6" r="4" fill="none" stroke="#9aa7a5" stroke-width="1.4"/><path d="M2 15 L12 15" stroke="#9aa7a5" stroke-width="1.4"/></svg>Istanbul, Turkey</div>
<div class="field" style="left:177px;top:3450px;width:157px">
  <svg width="14" height="14" viewBox="0 0 14 14"><rect x="1" y="2" width="12" height="11" fill="none" stroke="#9aa7a5" stroke-width="1.4"/></svg>Date in</div>
<div class="field" style="left:351px;top:3450px;width:160px">
  <svg width="14" height="14" viewBox="0 0 14 14"><circle cx="7" cy="7" r="6" fill="none" stroke="#9aa7a5" stroke-width="1.4"/><path d="M7 3v4h3" stroke="#9aa7a5" fill="none" stroke-width="1.4"/></svg>10:00 a.m.</div>
<div class="field" style="left:177px;top:3534px;width:157px">
  <svg width="14" height="14" viewBox="0 0 14 14"><rect x="1" y="2" width="12" height="11" fill="none" stroke="#9aa7a5" stroke-width="1.4"/></svg>Date Out</div>
<div class="field" style="left:351px;top:3534px;width:160px">
  <svg width="14" height="14" viewBox="0 0 14 14"><circle cx="7" cy="7" r="6" fill="none" stroke="#9aa7a5" stroke-width="1.4"/><path d="M7 3v4h3" stroke="#9aa7a5" fill="none" stroke-width="1.4"/></svg>12:00 p.m.</div>
<div class="field" style="left:177px;top:3615px;width:334px">
  <svg width="16" height="12" viewBox="0 0 16 12"><path d="M1 8 L15 8 L12 11 L4 11 Z M5 8 V2 L10 6" fill="none" stroke="#9aa7a5" stroke-width="1.3"/></svg>Boat Type
  <svg style="left:auto;right:10px;top:12px" width="10" height="6" viewBox="0 0 10 6"><path d="M1 1 L5 5 L9 1" fill="none" stroke="#777" stroke-width="1.3"/></svg></div>
<div class="field" style="left:177px;top:3694px;width:219px">
  <svg width="14" height="12" viewBox="0 0 14 12"><rect x="1" y="1" width="12" height="10" fill="none" stroke="#9aa7a5" stroke-width="1.3"/></svg>Payment Method
  <svg style="left:auto;right:8px;top:12px" width="10" height="6" viewBox="0 0 10 6"><path d="M1 1 L5 5 L9 1" fill="none" stroke="#777" stroke-width="1.3"/></svg></div>
<span class="pay" style="left:425px">Cardo</span>
<span class="pay" style="left:472px">Payra</span>
<div class="abs cta">CHARTER NOW!</div>

<div class="abs cal-head">August, 2020</div>
<svg class="abs" style="left:666px;top:3351px" width="12" height="18" viewBox="0 0 12 18"><path d="M10 2 L3 9 L10 16" fill="none" stroke="var(--deep)" stroke-width="2.4"/></svg>
<svg class="abs" style="left:1049px;top:3351px" width="12" height="18" viewBox="0 0 12 18"><path d="M2 2 L9 9 L2 16" fill="none" stroke="var(--deep)" stroke-width="2.4"/></svg>
<span class="dow" style="left:648px">S</span><span class="dow" style="left:715px">M</span><span class="dow" style="left:775px">T</span><span class="dow" style="left:841px">W</span><span class="dow" style="left:903px">T</span><span class="dow" style="left:965px">F</span><span class="dow" style="left:1028px">S</span>
<div class="abs range"></div>
<div class="days">
  <span class="day" style="left:960px;top:3463px">1</span><span class="day" style="left:1023px;top:3463px">2</span>
  <span class="day" style="left:649px;top:3525px">3</span><span class="day" style="left:710px;top:3525px">4</span><span class="day" style="left:775px;top:3525px">5</span><span class="day" style="left:836px;top:3525px">6</span><span class="day" style="left:898px;top:3525px">7</span><span class="day" style="left:960px;top:3525px">8</span><span class="day" style="left:1023px;top:3525px">9</span>
  <span class="day" style="left:643px;top:3586px">10</span><span class="day" style="left:710px;top:3586px">11</span><span class="day" style="left:770px;top:3586px">12</span><span class="day" style="left:836px;top:3586px">13</span><span class="day" style="left:898px;top:3586px">14</span><span class="day" style="left:960px;top:3586px">15</span><span class="day" style="left:1023px;top:3586px">16</span>
  <span class="day" style="left:643px;top:3648px">17</span><span class="day" style="left:710px;top:3648px">18</span><span class="day" style="left:770px;top:3648px">19</span><span class="day" style="left:836px;top:3648px">20</span><span class="day" style="left:898px;top:3648px">21</span><span class="day" style="left:960px;top:3648px">22</span><span class="day" style="left:1023px;top:3648px">23</span>
  <span class="day" style="left:643px;top:3710px">24</span><span class="day" style="left:710px;top:3710px">25</span><span class="day" style="left:770px;top:3710px">26</span><span class="day" style="left:836px;top:3710px">27</span><span class="day" style="left:898px;top:3710px">28</span><span class="day" style="left:960px;top:3710px">29</span><span class="day" style="left:1023px;top:3710px">30</span>
  <span class="day" style="left:1023px;top:3772px">31</span>
</div>

<footer class="abs footer">
  <div class="flogo">Velmoria</div>
  <div class="addr">Jalan Teratai 14,<br>Kotabaru, Indonesia<br>081-555-204-317</div>
  <span class="social" style="left:118px"></span>
  <span class="social" style="left:156px"></span>
  <span class="social" style="left:194px"></span>
  <span class="social" style="left:240px"></span>
  <div class="copy">© 2020. Velmoria Alright Reserve</div>
  <ul style="left:604px"><li>Facilities</li><li>Toys</li><li>Events</li><li>Crew</li><li>Inquiry</li></ul>
  <ul style="left:763px"><li>Snorkeling</li><li>Diving</li><li>Surfing</li><li>Zumflo</li></ul>
  <ul style="left:916px"><li>Blog</li><li>Newsletter</li></ul>
</footer>

</body>
</html>
```